Business Card

We would like a very clean corporate, two sided business card that conveys that we are a quality focused, reliable organisation that can make a business better. We focus on a cycle of continuous improvement for IT systems.

The brief is primarily clean and corporate, nothing overly complicated.

We sell IT services, IT support, server implementation, problem solving services to businesses in Australia.

Business

```html
<!DOCTYPE html>
<html lang="en">
<head>
<meta charset="utf-8">
<title>Corvalyn Systems – Business Card</title>
<link rel="stylesheet" href="https://fonts.googleapis.com/css2?family=Arimo:ital,wght@0,400;0,700;1,400&display=swap">
<style>
  :root {
    --brand-red: #c8144a;
    --ink: #2b2d3a;
    --paper: #ffffff;
    --backdrop: #e9e9e9;
    --on-red: #ffffff;
  }
  * { box-sizing: border-box; margin: 0; padding: 0; }
  html, body {
    width: 1200px;
    height: 900px;
    overflow: hidden;
    background: var(--backdrop);
    font-family: "Arimo", Arial, sans-serif;
    color: var(--ink);
  }
  .canvas { position: relative; width: 1200px; height: 900px; }
  .card {
    position: absolute;
    left: 307px;
    width: 586px;
    height: 326px;
    background: var(--paper);
    overflow: hidden;
  }
  .card--front { top: 67px; }
  .card--back { top: 504px; display: flex; }

  /* Front */
  .brand-mark {
    position: absolute;
    left: 70px;
    top: 140px;
    display: flex;
    align-items: center;
    gap: 14px;
  }
  .brand-mark__name {
    font-size: 56px;
    font-weight: 700;
    color: var(--ink);
    letter-spacing: -1px;
    line-height: 1;
  }
  .brand-mark__dot {
    width: 24px;
    height: 24px;
    border-radius: 50%;
    background: var(--brand-red);
  }
  .front-band {
    position: absolute;
    right: 0;
    bottom: 0;
    width: 338px;
    height: 41px;
    background: var(--brand-red);
  }

  /* Back */
  .holder {
    position: relative;
    width: 248px;
    height: 100%;
    padding: 30px 0 0 24px;
  }
  .holder__name { font-size: 24px; font-weight: 700; color: var(--ink); line-height: 1.1; }
  .holder__title { margin-top: 3px; font-size: 20px; font-style: italic; color: var(--brand-red); }
  .holder .brand-mark--small {
    position: absolute;
    left: 24px;
    top: 262px;
    display: flex;
    align-items: center;
    gap: 7px;
  }
  .brand-mark--small .brand-mark__name { font-size: 26px; letter-spacing: -0.5px; }
  .brand-mark--small .brand-mark__dot { width: 11px; height: 11px; }

  .contact-panel {
    flex: 1;
    background: var(--brand-red);
    color: var(--on-red);
    padding: 30px 20px 0 24px;
    position: relative;
  }
  .contact-panel__company { font-size: 22px; font-weight: 700; margin-bottom: 2px; }
  .contact-panel__address,
  .contact-panel__phones { font-size: 19px; line-height: 1.3; }
  .contact-panel__phones { margin-top: 12px; }
  .contact-panel__label { font-weight: 700; margin-right: 8px; }
  .contact-panel__rule {
    position: absolute;
    left: 24px;
    right: 0;
    top: 258px;
    border: 0;
    border-top: 2px solid var(--on-red);
  }
  .contact-panel__web {
    position: absolute;
    left: 24px;
    top: 272px;
    font-size: 21px;
    font-weight: 700;
  }
</style>
</head>
<body>
  <main class="canvas">
    <section class="card card--front" aria-label="Card front">
      <div class="brand-mark">
        <span class="brand-mark__name">Corvalyn</span>
        <span class="brand-mark__dot"></span>
      </div>
      <div class="front-band"></div>
    </section>

    <section class="card card--back" aria-label="Card back">
      <div class="holder">
        <p class="holder__name">Your Name</p>
        <p class="holder__title">Manager</p>
        <div class="brand-mark--small">
          <span class="brand-mark__name">Corvalyn</span>
          <span class="brand-mark__dot"></span>
        </div>
      </div>
      <div class="contact-panel">
        <p class="contact-panel__company">Corvalyn Systems Pty Ltd</p>
        <p class="contact-panel__address">Level 4, 88 Carrow Street<br>Eastwood Heights, NSW, 2199<br>Australia</p>
        <p class="contact-panel__phones">
          <span class="contact-panel__label">P</span>+61 2 5550 1184<br>
          <span class="contact-panel__label">F</span>+61 2 5550 1190
        </p>
        <hr class="contact-panel__rule">
        <p class="contact-panel__web">www.corvalynit.net</p>
      </div>
    </section>
  </main>
</body>
</html>
```